Autism Support Coach needs Advertisement Design

I need an ad that fits in the feel of the "Save the Date" picture attached below. My business will be a sponsor and also advertising in the gala's magazine. I would like my original colors of orange and maroon red to be the standout colors. Phone number, website and Chatterfold should be somewhere at the bottom maybe. I am open to variations of background color in the oranges and maroon reds if you think it will look good. Dimensions should be: 4-1/2”h x 6” w
Thank you!!!

Target Market(s)

Autism Fundraising Gala with a Ruby theme

Industry/Entity Type

Advertising

Font styles to use
Script

Requirements
Must have
• The tag line should be:
• Autism Support Coaching
• Phone: 734-615-2089
• torvelancoaching.com
• Follow us on Chatterfold.com/Torvelancoachingautism

```html
<!DOCTYPE html>
<html lang="en">
<head>
<meta charset="utf-8">
<title>Torvelan Coaching Services – Gala Advertisement</title>
<link href="https://fonts.googleapis.com/css2?family=Arimo:ital,wght@0,400;0,700;1,700&display=swap" rel="stylesheet">
<style>
  :root {
    --maroon: #b4261d;
    --orange: #f07c1e;
    --orange-deep: #e8591c;
    --orange-light: #f9a23a;
    --ink: #3b3b3b;
    --paper: #fbf8f3;
    --texture: #e6e2db;
    --white: #ffffff;
  }
  * { margin: 0; padding: 0; box-sizing: border-box; }
  html, body { width: 1200px; height: 900px; overflow: hidden; background: var(--paper); }
  body { font-family: "Arimo", Arial, sans-serif; color: var(--ink); }

  .ad { position: relative; width: 1200px; height: 900px; overflow: hidden; background: var(--paper); }

  .texture-area { position: absolute; left: 0; top: 0; width: 320px; height: 720px;
                  background: linear-gradient(90deg, var(--texture) 0%, rgba(251,248,243,0) 100%); }

  .copy { position: absolute; left: 147px; width: 1040px; text-align: center;
          line-height: 1; white-space: nowrap; }

  .section-title { color: var(--maroon); font-weight: 700; font-size: 44px; letter-spacing: 0.5px; }
  .feeling-now { color: var(--orange); font-weight: 700; font-style: italic; font-size: 26px; }
  .feeling-next { color: var(--orange); font-weight: 700; font-size: 33px; }
  .detail { font-size: 26px; color: var(--ink); }

  .imagine-rule { position: absolute; left: 300px; top: 350px; width: 734px; height: 60px; }

  .band { position: absolute; left: 0; top: 0; width: 1200px; height: 900px; }

  .brand-mark { position: absolute; left: 48px; top: 556px; width: 106px; height: 106px;
                border-radius: 50%; background: var(--white); }
  .brand-name { position: absolute; left: 34px; top: 716px; color: var(--white);
                font-weight: 700; font-size: 34px; line-height: 42px; white-space: nowrap; }
  .tagline { position: absolute; left: 34px; top: 818px; color: var(--white);
             font-size: 22px; line-height: 1; white-space: nowrap; }

  .contact { position: absolute; left: 423px; top: 760px; color: var(--white); white-space: nowrap; }
  .contact-line { font-size: 34px; line-height: 44px; }
  .contact-social { font-size: 22px; line-height: 1; margin-top: 10px; }
</style>
</head>
<body>
<main class="ad">
  <div class="texture-area" role="img" aria-label="Faint light grey puzzle-piece texture"></div>

  <h1 class="copy section-title" style="top:20px">ARE YOU FEELING:</h1>

  <p class="copy feeling-now" style="top:92px">Overwhelmed?</p>
  <p class="copy detail" style="top:120px">Your child's behavior seems unmanageable and you don't know where to turn?</p>

  <p class="copy feeling-now" style="top:173px">Helpless?</p>
  <p class="copy detail" style="top:201px">When your child acts out and people disapprove or stare?</p>

  <p class="copy feeling-now" style="top:265px">Anxious?</p>
  <p class="copy detail" style="top:293px">You don't know what will happen to your child if something happens to you?</p>

  <svg class="imagine-rule" viewBox="0 0 734 60" aria-hidden="true">
    <line x1="0" y1="30" x2="135" y2="30" stroke="var(--maroon)" stroke-width="3"/>
    <line x1="599" y1="30" x2="734" y2="30" stroke="var(--maroon)" stroke-width="3"/>
    <path d="M135 44 Q367 62 599 44" fill="none" stroke="var(--maroon)" stroke-width="3"/>
  </svg>
  <h2 class="copy section-title" style="top:359px">IMAGINE FEELING:</h2>

  <p class="copy feeling-next" style="top:423px">Confident and In Control</p>
  <p class="copy detail" style="top:460px">Calmly using new skills to handle any situation.</p>

  <p class="copy feeling-next" style="top:521px">Understood and Supported</p>
  <p class="copy detail" style="top:562px">Having fulfilling relationships with those close to you.</p>

  <p class="copy feeling-next" style="top:621px">Positive and Optimistic</p>
  <p class="copy detail" style="top:657px">Knowing the future is going to OK.</p>

  <svg class="band" viewBox="0 0 1200 900" aria-hidden="true">
    <defs>
      <linearGradient id="bandFill" x1="0" y1="0" x2="1" y2="0">
        <stop offset="0" stop-color="var(--orange-light)"/>
        <stop offset="0.5" stop-color="var(--orange)"/>
        <stop offset="1" stop-color="var(--orange-deep)"/>
      </linearGradient>
    </defs>
    <path d="M0 690 C300 650 650 705 900 735 C1030 750 1130 752 1200 748 L1200 900 L0 900 Z" fill="var(--orange-deep)"/>
    <path d="M0 704 C300 666 650 720 900 750 C1030 765 1130 768 1200 765 L1200 900 L0 900 Z" fill="url(#bandFill)"/>
  </svg>

  <div class="brand-mark"></div>
  <p class="brand-name">Torvelan<br>Coaching Services</p>
  <p class="tagline">Autism Support Coaching</p>

  <div class="contact">
    <p class="contact-line">734.615.2089</p>
    <p class="contact-line">www.torvelancoaching.com</p>
    <p class="contact-social">Follow us on Chatterfold.com/Torvelancoachingautism</p>
  </div>
</main>
</body>
</html>
```